Sales/Landing Page Redesign for Hunting product

I am looking for a redesign for https://ridgeholloworchard.com/quarter-pad .

We want to add in the information for our new XL quarterpad found: https://ridgeholloworchard.com/shop/hunting/xl-big-game-quarter-pad/

We also will be adding a spot for this video: https://www.vidstreamer.example/watch?v=Zt7kLq2wPnx

We like having the 3 options at the bottom, but the goal for this page is to sell the quarter pad.

Target Market(s)

Western Hunters, campers, outdoorsmen

Industry/Entity Type

Hunting

Number of Pages Required

1 page

Font styles to use
Sans Serif

Requirements
Must have
• a clean design that is geared to sell the product.

```html
<!DOCTYPE html>
<html lang="en">
<head>
<meta charset="utf-8">
<title>Trailhold Quarter Pads</title>
<link href="https://fonts.googleapis.com/css2?family=Montserrat:wght@400;500;600;700;800&family=Open+Sans:wght@400;600&display=swap" rel="stylesheet">
<style>
:root{
  --red:#e0101c;
  --red-dark:#9e0a12;
  --orange:#f5a40c;
  --ink:#0b0f14;
  --text:#2a2a2a;
  --muted:#6b6b6b;
  --card:#ececec;
  --white:#ffffff;
  --pad-red:#b3161c;
  --pad-orange:#f26a26;
  --pad-green:#1fa64a;
}
*{margin:0;padding:0;box-sizing:border-box}
html,body{width:1200px;height:3610px;overflow:hidden}
body{font-family:"Montserrat",sans-serif;color:var(--text);background:var(--white);position:relative}
.abs{position:absolute}
section,header,footer{position:absolute;left:0;width:1200px}

/* nav */
.site-nav{top:0;height:80px;background:var(--ink)}
.brand{left:144px;top:22px;font-weight:700;font-size:29px;letter-spacing:2px;color:var(--white)}
.nav-link{top:30px;font-size:15px;font-weight:600;color:var(--white)}
.nav-link.active{color:var(--orange)}
.shop-btn{left:854px;top:20px;width:127px;height:39px;background:var(--red);color:var(--white);font-size:15px;font-weight:600;display:flex;align-items:center;justify-content:center}
.cart-badge{left:1009px;top:20px}

/* hero */
.hero{top:80px;height:534px;overflow:hidden}
.hero-photo{left:0;top:0;width:1200px;height:534px;background:linear-gradient(120deg,#4d4a3c 0%,#6d6247 30%,#c0652a 55%,#5a4a3a 100%)}
.hero-text{right:146px;text-align:right;color:var(--white)}
.hero-kicker{top:30px;font-size:33px;font-weight:600;line-height:48px}
.hero-title{top:118px;font-size:82px;font-weight:800;line-height:90px}
.hero-rule{left:934px;top:210px;width:120px;height:3px;background:var(--orange)}
.hero-point{font-size:16px;font-weight:600;color:var(--white);display:flex;align-items:center;gap:10px;right:146px}
.hero-point::before{content:"";width:24px;height:1px;background:var(--white)}
.btn{display:flex;align-items:center;justify-content:center;font-weight:600;font-size:16px}
.btn-outline{border:1.5px solid var(--orange);color:var(--orange)}
.btn-solid{background:var(--orange);color:var(--ink)}
.btn-red{background:var(--red);color:var(--white)}

/* headings */
.section-title{font-size:32px;font-weight:700;color:var(--red);text-transform:uppercase}
.center{left:0;width:1200px;text-align:center}
.rule{height:3px;width:120px;background:var(--orange)}

/* still section */
.still{top:614px;height:592px}
.check-list{list-style:none}
.check-list li{display:flex;align-items:flex-start;gap:16px;font-size:20px;line-height:28px;height:48px}
.check-list svg{flex:none;margin-top:6px}
.photo-still{left:648px;top:81px;width:408px;height:429px;background:linear-gradient(180deg,#6d7f8d 0%,#3d4a52 40%,#d9682a 70%,#7a4a30 100%)}

/* guarantee */
.guarantee{top:1206px;height:270px;overflow:hidden}
.guarantee-photo{left:0;top:0;width:1200px;height:270px;background:linear-gradient(90deg,#6b4a2a 0%,#b48a52 45%,#e2c493 75%,#d8b27a 100%)}
.guarantee h2{left:587px;top:28px;font-size:33px;font-weight:700;color:var(--ink)}
.guarantee p{left:587px;top:84px;width:480px;font-family:"Open Sans",sans-serif;font-size:12.4px;line-height:24px;color:#2b2014}

/* products */
.choose{top:1476px;height:812px}
.product{width:448px;height:271px;background:linear-gradient(90deg,#f4f4f4,#e3e3e3)}
.bag{left:50px;top:40px;width:180px;height:190px;border-radius:12px 12px 40px 40px}
.product-color{left:257px;top:38px;font-size:32px;font-weight:700}
.product-type{left:257px;top:76px;font-size:19px;font-weight:700;color:var(--ink)}
.price{left:258px;top:115px;height:39px;padding:0 10px;background:var(--ink);color:var(--white);font-size:24px;font-weight:500;display:flex;align-items:center}
.cart-btn{left:258px;top:169px;width:56px;height:56px;border-radius:50%;background:var(--orange);display:flex;align-items:center;justify-content:center}

/* responsible */
.responsible{top:2288px;height:610px;overflow:hidden}
.butcher-photo{left:0;top:0;width:700px;height:610px;background:linear-gradient(160deg,#5b5a4c 0%,#9a7c63 35%,#a8323a 65%,#e2b0a8 100%)}
.responsible h2{left:690px;top:46px;font-size:31px;font-weight:700;line-height:40px;color:var(--white)}
.responsible .check-list li{color:var(--white)}

/* testimonials */
.reviews{top:2898px;height:569px}
.review{top:191px;width:298px;height:297px;background:var(--card)}
.quote-dot{left:22px;top:-20px;width:40px;height:40px;border-radius:50%;background:var(--orange);display:flex;align-items:center;justify-content:center;color:var(--red);font-weight:800;font-size:22px}
.review p{left:23px;top:50px;width:250px;font-family:"Open Sans",sans-serif;font-size:13px;line-height:25.5px;color:#333}
.review .rule{left:23px;top:191px}
.review .name{left:23px;top:216px;font-size:16.5px;font-weight:600;color:var(--red);line-height:25px}

/* footer */
.site-footer{top:3467px;height:143px;background:var(--ink)}
.foot-line{left:146px;font-family:"Open Sans",sans-serif;font-size:11.5px;color:#7f8790}
.social{width:34px;height:34px;border:1.5px solid #6f7780;border-radius:50%}
.pay{width:34px;height:21px;background:#c9ccd1;border-radius:2px}
</style>
</head>
<body>

<header class="site-nav">
  <div class="abs brand">TRAILHOLD</div>
  <a class="abs nav-link active" style="left:597px">MEALS</a>
  <a class="abs nav-link" style="left:692px">QUARTER PADS</a>
  <a class="abs shop-btn">SHOP NOW</a>
  <svg class="abs cart-badge" width="50" height="40" viewBox="0 0 50 40" aria-label="Cart">
    <circle cx="26" cy="19" r="18" fill="#e0101c"/>
    <path d="M18 13h3l2 9h9l2-7H22" fill="none" stroke="#fff" stroke-width="2.2"/>
    <circle cx="24" cy="26" r="1.6" fill="#fff"/><circle cx="31" cy="26" r="1.6" fill="#fff"/>
    <circle cx="8" cy="9" r="8" fill="#f5a40c"/>
    <text x="8" y="12" font-size="9" text-anchor="middle" fill="#0b0f14" font-family="Montserrat">0</text>
  </svg>
</header>

<section class="hero">
  <div class="abs hero-photo" role="img" aria-label="Hunter kneeling beside game quarters laid out on an orange quarter pad, viewed from above"></div>
  <svg class="abs" style="left:0;top:0" width="1200" height="534" viewBox="0 0 1200 534">
    <polygon points="575,0 1200,0 1200,534 780,534" fill="#e0101c"/>
    <polygon points="575,0 780,534 700,534" fill="#b30c16" opacity=".85"/>
    <polygon points="900,534 1200,300 1200,534" fill="#c10d17"/>
    <circle cx="600" cy="266" r="40" fill="none" stroke="#fff" stroke-width="3"/>
    <polygon points="588,246 588,286 620,266" fill="#fff"/>
  </svg>
  <div class="abs hero-text hero-kicker">QUARTER PADS TO<br>KEEP YOUR MEAT</div>
  <div class="abs hero-text hero-title">CLEAN</div>
  <div class="abs hero-rule"></div>
  <div class="abs hero-point" style="top:225px">100% Waterproof</div>
  <div class="abs hero-point" style="top:257px">Lightweight</div>
  <div class="abs hero-point" style="top:289px">Quality Guarantee</div>
  <a class="abs btn btn-outline" style="left:876px;top:335px;width:178px;height:46px">LEARN MORE</a>
  <a class="abs btn btn-solid" style="left:876px;top:398px;width:178px;height:46px">BUY NOW</a>
</section>

<section class="still">
  <h2 class="abs section-title" style="left:142px;top:74px">DO YOU STILL...</h2>
  <div class="abs rule" style="left:144px;top:136px"></div>
  <ul class="abs check-list" style="left:144px;top:166px">
    <li><svg width="16" height="16" viewBox="0 0 16 16"><circle cx="8" cy="8" r="8" fill="#e0101c"/><path d="M4.5 8.2l2.3 2.3 4.5-4.6" stroke="#fff" stroke-width="2" fill="none"/></svg>Lay your fresh meat on a rock?</li>
    <li><svg width="16" height="16" viewBox="0 0 16 16"><circle cx="8" cy="8" r="8" fill="#e0101c"/><path d="M4.5 8.2l2.3 2.3 4.5-4.6" stroke="#fff" stroke-width="2" fill="none"/></svg>Sew bed sheets together?</li>
    <li><svg width="16" height="16" viewBox="0 0 16 16"><circle cx="8" cy="8" r="8" fill="#e0101c"/><path d="M4.5 8.2l2.3 2.3 4.5-4.6" stroke="#fff" stroke-width="2" fill="none"/></svg>Use a blue tarp?</li>
    <li><svg width="16" height="16" viewBox="0 0 16 16"><circle cx="8" cy="8" r="8" fill="#e0101c"/><path d="M4.5 8.2l2.3 2.3 4.5-4.6" stroke="#fff" stroke-width="2" fill="none"/></svg>Lay your meat in the dirt?</li>
    <li><svg width="16" height="16" viewBox="0 0 16 16"><circle cx="8" cy="8" r="8" fill="#e0101c"/><path d="M4.5 8.2l2.3 2.3 4.5-4.6" stroke="#fff" stroke-width="2" fill="none"/></svg>Stuff the meat in old used pillow cases?</li>
  </ul>
  <p class="abs" style="left:143px;top:410px;font-size:20px">...There is a better way</p>
  <a class="abs btn btn-red" style="left:144px;top:463px;width:256px;height:47px">SELECT MY QUARTER PAD</a>
  <div class="abs photo-still" role="img" aria-label="Hunter by a mountain lake with game quarters resting on an orange quarter pad"></div>
</section>

<section class="guarantee">
  <div class="abs guarantee-photo" role="img" aria-label="Bull elk standing in golden grass at sunrise"></div>
  <svg class="abs" style="left:0;top:0" width="600" height="270" viewBox="0 0 600 270">
    <polygon points="0,0 225,0 0,270" fill="#e0101c"/>
    <polygon points="65,0 225,0 140,110" fill="#a00a13"/>
    <polygon points="0,150 120,270 0,270" fill="#c40d17"/>
  </svg>
  <h2 class="abs">100% QUALITY GUARANTEE</h2>
  <p class="abs">We've designed our Quarter Pads for maximum performance and durability so you can keep the meat you harvest in the backcountry clean and out of the dirt. If you are at all unsatisfied, contact us and we'll make it right.</p>
  <a class="abs btn btn-solid" style="left:587px;top:172px;width:180px;height:48px">BUY NOW</a>
</section>

<section class="choose">
  <h2 class="abs section-title center" style="top:74px">CHOOSE YOUR QUARTER PAD</h2>
  <div class="abs rule" style="left:540px;top:136px"></div>

  <div class="abs product" style="left:144px;top:171px">
    <div class="abs bag" style="background:var(--pad-red)" role="img" aria-label="Red quarter pad in its stuff sack"></div>
    <div class="abs product-color" style="color:var(--pad-red)">RED</div>
    <div class="abs product-type">QUARTER PAD</div>
    <div class="abs price">$19.99</div>
    <div class="abs cart-btn"><svg width="22" height="20" viewBox="0 0 22 20"><path d="M1 2h4l2 10h11l2-8H6" fill="none" stroke="#0b0f14" stroke-width="2.4"/><circle cx="8" cy="16" r="2" fill="#0b0f14"/><circle cx="17" cy="16" r="2" fill="#0b0f14"/></svg></div>
  </div>

  <div class="abs product" style="left:608px;top:171px">
    <div class="abs bag" style="background:var(--pad-orange)" role="img" aria-label="Orange quarter pad in its stuff sack"></div>
    <div class="abs product-color" style="color:var(--pad-orange)">ORANGE</div>
    <div class="abs product-type">QUARTER PAD</div>
    <div class="abs price">$19.99</div>
    <div class="abs cart-btn"><svg width="22" height="20" viewBox="0 0 22 20"><path d="M1 2h4l2 10h11l2-8H6" fill="none" stroke="#0b0f14" stroke-width="2.4"/><circle cx="8" cy="16" r="2" fill="#0b0f14"/><circle cx="17" cy="16" r="2" fill="#0b0f14"/></svg></div>
  </div>

  <div class="abs product" style="left:144px;top:460px">
    <div class="abs bag" style="background:var(--pad-orange)" role="img" aria-label="Orange XL quarter pad in its stuff sack"></div>
    <div class="abs product-color" style="color:var(--pad-orange)">ORANGE</div>
    <div class="abs product-type">XL QUARTER PAD</div>
    <div class="abs price">$29.99</div>
    <div class="abs cart-btn"><svg width="22" height="20" viewBox="0 0 22 20"><path d="M1 2h4l2 10h11l2-8H6" fill="none" stroke="#0b0f14" stroke-width="2.4"/><circle cx="8" cy="16" r="2" fill="#0b0f14"/><circle cx="17" cy="16" r="2" fill="#0b0f14"/></svg></div>
  </div>

  <div class="abs product" style="left:608px;top:460px">
    <div class="abs bag" style="background:var(--pad-green)" role="img" aria-label="Green quarter pad in its stuff sack"></div>
    <div class="abs product-color" style="color:var(--pad-green)">GREEN</div>
    <div class="abs product-type">QUARTER PAD</div>
    <div class="abs price">$19.99</div>
    <div class="abs cart-btn"><svg width="22" height="20" viewBox="0 0 22 20"><path d="M1 2h4l2 10h11l2-8H6" fill="none" stroke="#0b0f14" stroke-width="2.4"/><circle cx="8" cy="16" r="2" fill="#0b0f14"/><circle cx="17" cy="16" r="2" fill="#0b0f14"/></svg></div>
  </div>
</section>

<section class="responsible">
  <div class="abs butcher-photo" role="img" aria-label="Hunter's hands trimming fresh game meat with an orange knife"></div>
  <svg class="abs" style="left:0;top:0" width="1200" height="610" viewBox="0 0 1200 610">
    <polygon points="641,0 1200,0 1200,610 562,610" fill="#fff"/>
    <polygon points="647,0 1200,0 1200,610 568,610" fill="#e0101c"/>
  </svg>
  <h2 class="abs">BE RESPONSIBLE.<br>USE A QUARTER PAD.</h2>
  <div class="abs rule" style="left:690px;top:150px"></div>
  <ul class="abs check-list" style="left:690px;top:179px;width:380px">
    <li><svg width="16" height="16" viewBox="0 0 16 16"><circle cx="8" cy="8" r="8" fill="#f5a40c"/><path d="M4.5 8.2l2.3 2.3 4.5-4.6" stroke="#e0101c" stroke-width="2" fill="none"/></svg>Keep your meat off the dirt</li>
    <li><svg width="16" height="16" viewBox="0 0 16 16"><circle cx="8" cy="8" r="8" fill="#f5a40c"/><path d="M4.5 8.2l2.3 2.3 4.5-4.6" stroke="#e0101c" stroke-width="2" fill="none"/></svg>Lightweight</li>
    <li><svg width="16" height="16" viewBox="0 0 16 16"><circle cx="8" cy="8" r="8" fill="#f5a40c"/><path d="M4.5 8.2l2.3 2.3 4.5-4.6" stroke="#e0101c" stroke-width="2" fill="none"/></svg>100% Waterproof</li>
    <li><svg width="16" height="16" viewBox="0 0 16 16"><circle cx="8" cy="8" r="8" fill="#f5a40c"/><path d="M4.5 8.2l2.3 2.3 4.5-4.6" stroke="#e0101c" stroke-width="2" fill="none"/></svg>Reusable</li>
    <li><svg width="16" height="16" viewBox="0 0 16 16"><circle cx="8" cy="8" r="8" fill="#f5a40c"/><path d="M4.5 8.2l2.3 2.3 4.5-4.6" stroke="#e0101c" stroke-width="2" fill="none"/></svg>55"X60" WHEN OPEN</li>
    <li style="height:auto"><svg width="16" height="16" viewBox="0 0 16 16"><circle cx="8" cy="8" r="8" fill="#f5a40c"/><path d="M4.5 8.2l2.3 2.3 4.5-4.6" stroke="#e0101c" stroke-width="2" fill="none"/></svg>Respect the animal by keeping it contamination free.</li>
  </ul>
  <a class="abs btn btn-solid" style="left:690px;top:496px;width:256px;height:47px">SELECT MY QUARTER PAD</a>
</section>

<section class="reviews">
  <h2 class="abs section-title center" style="top:73px">WHAT OTHERS ARE SAYING...</h2>
  <div class="abs rule" style="left:540px;top:136px"></div>

  <svg class="abs" style="left:52px;top:329px" width="20" height="30" viewBox="0 0 20 30"><path d="M15 3L5 15l10 12" fill="none" stroke="#555" stroke-width="3"/></svg>
  <svg class="abs" style="left:1126px;top:329px" width="20" height="30" viewBox="0 0 20 30"><path d="M5 3l10 12L5 27" fill="none" stroke="#555" stroke-width="3"/></svg>

  <div class="abs review" style="left:144px">
    <div class="abs quote-dot">“</div>
    <p class="abs">This is something that is needed on every hunt! Light easy to carry and a necessity to keep your hard earned meat clean!</p>
    <div class="abs rule"></div>
    <div class="abs name">Cal Whitmore</div>
  </div>
  <div class="abs review" style="left:451px">
    <div class="abs quote-dot">“</div>
    <p class="abs">The Quarter Pad is a game changer when it comes to cleanliness in the hills. Lightweight, and compacts down super small! No more getting dirt and pine needles all over your meat.</p>
    <div class="abs rule"></div>
    <div class="abs name">Dane Varholm<br>@HIGHCOUNTRYTRAIL</div>
  </div>
  <div class="abs review" style="left:758px">
    <div class="abs quote-dot">“</div>
    <p class="abs">The Quarter Pads keep your meat clean and double up as a waterproof poncho and ground tarp. They are a must have for any serious hunter.</p>
    <div class="abs rule"></div>
    <div class="abs name">Wes Ardell</div>
  </div>
</section>

<footer class="site-footer">
  <div class="abs foot-line" style="top:31px">Meals &nbsp;|&nbsp; Quarter Pads &nbsp;|&nbsp; My Account &nbsp;|&nbsp; Blog</div>
  <div class="abs foot-line" style="top:63px">Terms of Service Agreement &nbsp;|&nbsp; Refund and Return Policy &nbsp;|&nbsp; Privacy Policy Agreement</div>
  <div class="abs foot-line" style="top:95px">Copyright © 2020 Trailhold Outdoors. &nbsp;All rights reserved.</div>
  <div class="abs social" style="left:974px;top:34px"></div>
  <div class="abs social" style="left:1022px;top:34px"></div>
  <div class="abs pay" style="left:898px;top:86px"></div>
  <div class="abs pay" style="left:940px;top:86px"></div>
  <div class="abs pay" style="left:982px;top:86px"></div>
  <div class="abs pay" style="left:1024px;top:86px"></div>
</footer>

</body>
</html>
```